Roofing company in Toronto, Canada needs a logo design and business card design

We need a business card and logo created for our company. Our company is "KVL Roofing" which provides roofing services for commercial and residential customers. We serve customers in the Greater Toronto Area (in Canada) thus the name KVL.

We want the logo and business card to be a modern design displaying professionalism and quality in the work. We would prefer rounded corners for the business cards but are open to other ideas. The cards should be pleasant and appealing to customers.

Target Market(s)

Commercial and Residential customers

Industry/Entity Type

Roofing

Contact Information for Business Card

Logo Text

KVL Roofing

Requirements
Nice to have
• Colours that are pleasing to the eye but at the same time should stand out from other business cards. If the design can incorporate the name of KVL Roofing and the actual concept of roofing that would be nice.
Should not have
• Do not want the business cards or logo to be childish looking. Need to look professionally designed.

```html
<!DOCTYPE html>
<html lang="en">
<head>
<meta charset="UTF-8">
<title>KVL Roofing – Business Card</title>
<link rel="stylesheet" href="https://fonts.googleapis.com/css2?family=Open+Sans:wght@400;600;700&display=swap">
<style>
  :root {
    --backdrop: #1b1b1b;
    --card: #262626;
    --card-edge: #303030;
    --white: #f2f2f2;
    --muted: #b9b9b9;
    --yellow: #f1c83b;
    --divider: #6a6a6a;
  }
  * { margin: 0; padding: 0; box-sizing: border-box; }
  html, body {
    width: 1200px;
    height: 1000px;
    overflow: hidden;
    background: var(--backdrop);
    font-family: "Open Sans", Arial, sans-serif;
  }
  .canvas { position: relative; width: 1200px; height: 1000px; }

  .card {
    position: absolute;
    width: 560px;
    height: 320px;
    background: linear-gradient(160deg, var(--card-edge), var(--card) 60%);
    border-radius: 26px;
    box-shadow: 0 18px 40px rgba(0,0,0,0.55);
  }
  .card-front { left: 80px; top: 130px; }
  .card-back  { left: 560px; top: 540px; }

  /* Front: wordmark */
  .brand {
    position: absolute;
    inset: 0;
    display: flex;
    align-items: center;
    justify-content: center;
    gap: 14px;
  }
  .brand-mark {
    width: 26px;
    height: 26px;
    background: var(--yellow);
  }
  .brand-name {
    font-weight: 700;
    font-size: 40px;
    color: var(--white);
    letter-spacing: 1px;
    text-transform: uppercase;
  }

  /* Back: identity */
  .identity {
    position: absolute;
    left: 40px;
    top: 118px;
    width: 230px;
    text-align: right;
  }
  .person-name {
    font-weight: 700;
    font-size: 27px;
    color: var(--white);
    line-height: 1.1;
    letter-spacing: 0.5px;
  }
  .person-role {
    font-weight: 600;
    font-size: 14px;
    color: var(--yellow);
    letter-spacing: 0.6px;
    margin-top: 4px;
  }
  .divider {
    position: absolute;
    left: 290px;
    top: 100px;
    width: 1px;
    height: 90px;
    background: var(--divider);
  }
  .contacts {
    position: absolute;
    left: 310px;
    top: 104px;
    list-style: none;
  }
  .contact {
    display: flex;
    align-items: center;
    gap: 12px;
    font-size: 14px;
    color: var(--muted);
    height: 26px;
  }
  .contact svg { width: 13px; height: 13px; fill: var(--yellow); flex: none; }
  .contact .accent { color: var(--yellow); }

  .address {
    position: absolute;
    left: 310px;
    top: 252px;
    display: flex;
    align-items: center;
    gap: 10px;
    font-size: 14px;
    color: var(--muted);
  }
  .address svg { width: 12px; height: 15px; fill: var(--yellow); }
</style>
</head>
<body>
<div class="canvas">

  <section class="card card-front">
    <div class="brand">
      <span class="brand-mark"></span>
      <span class="brand-name">KVL Roofing</span>
    </div>
  </section>

  <section class="card card-back">
    <div class="identity">
      <p class="person-name">DANIEL REYES</p>
      <p class="person-role">CEO &amp; FOUNDER</p>
    </div>

    <div class="divider"></div>

    <ul class="contacts">
      <li class="contact">
        <svg viewBox="0 0 24 24" aria-hidden="true"><path d="M6.6 10.8a15.1 15.1 0 0 0 6.6 6.6l2.2-2.2c.3-.3.7-.4 1-.2 1.1.4 2.3.6 3.6.6.6 0 1 .4 1 1V20c0 .6-.4 1-1 1A17 17 0 0 1 3 4c0-.6.4-1 1-1h3.5c.6 0 1 .4 1 1 0 1.3.2 2.5.6 3.6.1.3 0 .7-.2 1z"/></svg>
        <span>+000 123 456 789</span>
      </li>
      <li class="contact">
        <svg viewBox="0 0 24 24" aria-hidden="true"><path d="M2 5h20v14H2zM4 7v.4l8 5.2 8-5.2V7zm0 2.8V17h16V9.8l-8 5.2z"/></svg>
        <span>yourname@email.com</span>
      </li>
      <li class="contact">
        <svg viewBox="0 0 24 24" aria-hidden="true"><path d="M12 2a10 10 0 1 0 0 20 10 10 0 0 0 0-20zm6.9 6h-3a15.6 15.6 0 0 0-1.3-3.9A8 8 0 0 1 18.9 8zM12 4c.8 1.2 1.5 2.5 1.9 4h-3.8c.4-1.5 1.1-2.8 1.9-4zM4.3 14a8.2 8.2 0 0 1 0-4h3.4a16 16 0 0 0 0 4zm.8 2h3a15.6 15.6 0 0 0 1.3 3.9A8 8 0 0 1 5.1 16zm3-8h-3a8 8 0 0 1 4.3-3.9C8.8 5.3 8.4 6.6 8.1 8zM12 20c-.8-1.2-1.5-2.5-1.9-4h3.8c-.4 1.5-1.1 2.8-1.9 4zm2.3-6H9.7a14.7 14.7 0 0 1 0-4h4.6a14.7 14.7 0 0 1 0 4zm.3 5.9c.6-1.2 1-2.5 1.3-3.9h3a8 8 0 0 1-4.3 3.9zm1.7-5.9a16 16 0 0 0 0-4h3.4a8.2 8.2 0 0 1 0 4z"/></svg>
        <span>www.<span class="accent">yoursitename</span>.com</span>
      </li>
    </ul>

    <div class="address">
      <svg viewBox="0 0 20 26" aria-hidden="true"><path d="M10 0a10 10 0 0 0-10 10c0 7.5 10 16 10 16s10-8.5 10-16A10 10 0 0 0 10 0zm0 14a4 4 0 1 1 0-8 4 4 0 0 1 0 8z"/></svg>
      <span>Your Street Address, Singapore, 1234</span>
    </div>
  </section>

</div>
</body>
</html>
```